EILT: Landing Page - EXPRESS VERSAND
Zielgruppe
Es soll in kurzer Zeit (max 48 Stunden) eine kleine Ladingpage entstehen. Expressversand / Import von China nach Deutschland . Aufgrund der stark steigenden Luftfrachtraten aus China heraus hat sich unsere Firma Fracht-Kapazitäten gesichert. Diese sollen nun angeboten werden. Über eine Ladingpage sollen Anfragen generiert werden. Diese Anfragen werden dann mit einem Angebot von uns beantwortet. Expressversand / Import von China nach Deutschland
Aufgabenstellung
Die Seite soll beinhalten:
- 1-2 Bilder (z. B. Luftfracht, Logistik, Flugzeug, Cargo, etc)
- kurzer erklärender Text: z.B. 'jetzt Angebot anfordern und günstig aus China per Express versenden.' Inkl. Abholung, Verzollung und Zustellung. Kurze Laufzeit von nur 3-5 Tagen. ab 45€ / Paket
- Anfrage Formular, bestehend aus: , Abholadresse in China/Post Code, ZielAdresse Deutschland, Sendungsinformationen (wie viele Kartons, wie schwer ist ein Karton und welche Abmessungen L/B/H ), wann ist die Sendung in China abholbereit, optional: Sendungsinhalt (Ware, Zolltarifnummer/HS Code) , Firma, Name, email adresse
- optional ein Header/Laufband etc mit: Bis zum 19. Nov 21 versenden - Ware bis MegaSonntag erhalten!
- 24h Servicehotline, Tel: 0987/314265
- 2-3 Kundenreferenzen: Bilder von Personen mit Text : „Schneller Versand - nur 4 Tage Laufzeit“ , „1A Service, ohne Probleme“ , „gute Preise - nur zu empfehlen.“
Unser Firmenlogo kann - muss aber nicht auftauchen.
In der farblichen Gestaltung haben Sie freie Hand und freuen uns auf Ihre Vorschläge.
Aufgrund der Dringlichkeit sollte diese Landingpage innerhalb 48 Stunden 'live ' gehen.
WICHTIG: Die Page sollte von Ihnen auch veröffentlich werden. Aktuell nutzen wir den Kelvo Homepagebaukasten. Die Page kann aber auch durch andere Anbieter veröffentlicht werden , zb Pagerune

```html
<!DOCTYPE html>
<html lang="de">
<head>
<meta charset="utf-8">
<title>Feronix Services – Expressversand China nach Deutschland</title>
<link href="https://fonts.googleapis.com/css2?family=Source+Sans+3:wght@400;600;700&display=swap" rel="stylesheet">
<style>
  :root {
    --bg-top: #0b3947;
    --bg-bottom: #032833;
    --accent-blue: #2ba3db;
    --accent-red: #e85440;
    --field-bg: #05222c;
    --card-bg: #1b3f4b;
    --quote: #1d4653;
    --text: #ffffff;
    --text-soft: #e3ecef;
    --star: #f6b73c;
    --rule: #24505c;
    --hero-warm: #8a6a52;
    --hero-cool: #2f6a80;
  }
  * { box-sizing: border-box; margin: 0; padding: 0; }
  html, body { width: 1200px; height: 1116px; overflow: hidden; }
  body {
    font-family: "Source Sans 3", sans-serif;
    color: var(--text);
    background: linear-gradient(180deg, var(--bg-top) 0%, #073341 45%, var(--bg-bottom) 100%);
    position: relative;
  }
  .hero-visual {
    position: absolute; left: 540px; top: 0; width: 660px; height: 480px;
    background: linear-gradient(225deg, var(--hero-warm) 0%, var(--hero-cool) 45%, rgba(11,57,71,0) 80%);
    opacity: 0.85;
  }
  .brand {
    position: absolute; left: 150px; top: 14px;
    display: flex; align-items: center; gap: 8px;
  }
  .brand-dot { width: 48px; height: 48px; border-radius: 50%; background: var(--accent-blue); }
  .brand-name { font-size: 36px; font-weight: 700; letter-spacing: 0.2px; }
  .hotline {
    position: absolute; left: 671px; top: 26px; width: 378px; height: 40px;
    background: var(--accent-blue); border-radius: 2px;
    font-size: 21px; font-weight: 700; text-align: center; line-height: 40px;
  }
  .headline {
    position: absolute; left: 150px; top: 152px;
    font-size: 41px; font-weight: 700; line-height: 48px;
  }
  .phone {
    position: absolute; left: 150px; top: 280px;
    font-size: 39px; font-weight: 700; color: var(--accent-blue);
  }
  .offer {
    position: absolute; left: 200px; top: 396px; width: 800px; height: 72px;
    background: var(--accent-red); border-radius: 3px;
    font-size: 17.5px; font-weight: 600; line-height: 27px; text-align: center;
    padding-top: 9px;
  }
  .offer::after {
    content: ""; position: absolute; left: 388px; bottom: -16px;
    border-left: 12px solid transparent; border-right: 12px solid transparent;
    border-top: 16px solid var(--accent-red);
  }
  .request-form {
    position: absolute; left: 202px; top: 494px; width: 797px;
    display: grid; grid-template-columns: 249px 249px 249px; column-gap: 25px; row-gap: 14px;
  }
  .field label { display: block; font-size: 13px; color: var(--text-soft); margin-bottom: 8px; padding-left: 2px; }
  .field input {
    width: 249px; height: 40px; background: var(--field-bg);
    border: 1.5px solid var(--accent-blue); border-radius: 3px; color: var(--text);
  }
  .submit {
    position: absolute; left: 477px; top: 753px; width: 250px; height: 40px;
    background: var(--accent-red); border: 0; border-radius: 2px; color: var(--text);
    font-family: inherit; font-size: 18px; font-weight: 600;
    display: flex; align-items: center; justify-content: center; gap: 10px;
  }
  .quote-mark {
    position: absolute; left: 146px; top: 808px;
    font-size: 130px; font-weight: 700; line-height: 1; color: var(--quote);
  }
  .testimonials { position: absolute; left: 153px; top: 901px; display: flex; gap: 14px; }
  .testimonial {
    width: 289px; height: 126px; background: var(--card-bg); border-radius: 2px;
    text-align: center; padding-top: 14px;
  }
  .testimonial-text { font-size: 15.5px; color: var(--text-soft); }
  .reviewer { display: flex; justify-content: center; align-items: center; gap: 8px; margin-top: 12px; }
  .avatar { width: 54px; height: 54px; border-radius: 50%; background: linear-gradient(160deg, #6b4a3a, #2c2421); }
  .reviewer-info { text-align: left; }
  .reviewer-name { font-size: 13px; }
  .stars { color: var(--star); font-size: 12px; letter-spacing: 1px; }
  .footer-rule { position: absolute; left: 153px; top: 1069px; width: 899px; height: 1px; background: var(--rule); }
  .copyright { position: absolute; left: 0; width: 1200px; top: 1082px; text-align: center; font-size: 13px; color: var(--text-soft); }
</style>
</head>
<body>
  <div class="hero-visual" role="img" aria-label="Luftaufnahme: Frachtflugzeug über dem Meer neben einem Containerschiff im Hafen"></div>

  <header>
    <div class="brand"><span class="brand-dot"></span><span class="brand-name">Feronix Services</span></div>
    <div class="hotline">24h Servicehotline, Tel: 0987/314265</div>
  </header>

  <h1 class="headline">Expressversand / Import<br>von China nach Deutschland</h1>
  <p class="phone">Tel: 0987/314265</p>

  <p class="offer">jetzt Angebot anfordern und günstig aus China per Express versenden.' Inkl. Abholung,<br>Verzollung und Zustellung. Kurze Laufzeit von nur 3-5 Tagen. ab 45€ / Paket</p>

  <form class="request-form">
    <div class="field"><label>Firma</label><input type="text"></div>
    <div class="field"><label>Name</label><input type="text"></div>
    <div class="field"><label>Email Adresse</label><input type="email"></div>
    <div class="field"><label>Abholadresse in China</label><input type="text"></div>
    <div class="field"><label>Post Code</label><input type="text"></div>
    <div class="field"><label>ZielAdresse Deutschland</label><input type="text"></div>
    <div class="field"><label>Wie Viele Kartons</label><input type="text"></div>
    <div class="field"><label>Karton Gewicht</label><input type="text"></div>
    <div class="field"><label>Abmessungen&nbsp; L / W / H</label><input type="text"></div>
  </form>

  <button class="submit" type="button">
    <svg width="18" height="18" viewBox="0 0 24 24" fill="none" stroke="#fff" stroke-width="1.6" stroke-linejoin="round"><path d="M22 2 2 11l8 3 3 8z"/><path d="M22 2 10 14"/></svg>
    SENDEN
  </button>

  <div class="quote-mark" aria-hidden="true">“</div>

  <section class="testimonials">
    <article class="testimonial">
      <p class="testimonial-text">Schneller Versand - nur 4 Tage Laufzeit</p>
      <div class="reviewer"><span class="avatar" role="img" aria-label="Porträtfoto des Kunden"></span><div class="reviewer-info"><div class="reviewer-name">Rufen Marsk</div><div class="stars">★★★★★</div></div></div>
    </article>
    <article class="testimonial">
      <p class="testimonial-text">1A Service, ohne Probleme</p>
      <div class="reviewer"><span class="avatar" role="img" aria-label="Porträtfoto des Kunden"></span><div class="reviewer-info"><div class="reviewer-name">Tobin Arell</div><div class="stars">★★★★★</div></div></div>
    </article>
    <article class="testimonial">
      <p class="testimonial-text">Gute Preise - nur zu empfehlen.</p>
      <div class="reviewer"><span class="avatar" role="img" aria-label="Porträtfoto des Kunden"></span><div class="reviewer-info"><div class="reviewer-name">Rufen Marsk</div><div class="stars">★★★★★</div></div></div>
    </article>
  </section>

  <div class="footer-rule"></div>
  <footer class="copyright">Copyright 2021. Alle Rechte vorbehalten.</footer>
</body>
</html>
```